Business Cards that are elegant and wow

I want to create and print business cards that represent my brand and stand out from the rest. We want to ensure they stay in our branding and the integrity is not lost. I am happy to look at different shapes like square etc.

It will be printed on very thick cards and will be stylish .

I want to create and print business cards that represent my brand and stand out from the rest. We want to ensure they stay in ur branding and the integrity is not lost. I am happy to look at different shapes like square etc.

Target Market(s)

real estate professionals

Industry/Entity Type

Real Estate

Contact Information for Business Card

Maren Holt
hello@brightfernrealty.com.au
brightfernrealty.com.au
0487 316 252 (SMS)

Colors

Designer to choose colors to be used in the design.

Requirements
Must have
• My logo
• email
• website
• Name
Nice to have
• I like the idea of printing with foil or spot gloss. You want it to stand out in a sea.
Should not have
• I would like you to stay in my colour themes. Don't change the colour of my logo

```html
<!DOCTYPE html>
<html lang="en">
<head>
<meta charset="utf-8">
<title>Bright Fern Realty – Business Card</title>
<link rel="stylesheet" href="https://fonts.googleapis.com/css2?family=Montserrat:wght@600;700&display=swap">
<style>
  :root {
    --page: #ffffff;
    --brand-pink: #f0035a;
    --brand-cyan: #00a0c6;
    --white: #ffffff;
  }
  * { margin: 0; padding: 0; box-sizing: border-box; }
  html, body {
    width: 1200px;
    height: 1000px;
    overflow: hidden;
    background: var(--page);
  }
  .canvas {
    position: relative;
    width: 1200px;
    height: 1000px;
    font-family: "Montserrat", sans-serif;
  }
  .card {
    position: absolute;
    left: 143px;
    top: 237px;
    width: 915px;
    height: 526px;
    background: var(--brand-pink);
    overflow: hidden;
  }
  .logo-frame {
    position: absolute;
    left: -2px;
    top: 201px;
    width: 414px;
    height: 125px;
    border: 1.5px solid var(--brand-cyan);
  }
  .logo-panel {
    position: absolute;
    left: 0;
    top: 212px;
    width: 394px;
    height: 102px;
    background: var(--white);
    display: flex;
    align-items: center;
    padding-left: 32px;
    gap: 14px;
  }
  .logo-dot {
    width: 44px;
    height: 44px;
    border-radius: 50%;
    background: var(--brand-pink);
    flex: none;
  }
  .logo-name {
    font-weight: 700;
    font-size: 27px;
    letter-spacing: 0.5px;
    color: var(--brand-cyan);
    white-space: nowrap;
  }
  .name-band {
    position: absolute;
    left: 394px;
    top: 239px;
    width: 521px;
    height: 46px;
    background: var(--brand-cyan);
    display: flex;
    align-items: center;
    justify-content: flex-end;
    padding-right: 52px;
  }
  .person-name {
    font-weight: 600;
    font-size: 34px;
    letter-spacing: 4px;
    color: var(--white);
    text-transform: uppercase;
    line-height: 1;
  }
  .contact {
    position: absolute;
    right: 53px;
    top: 324px;
    text-align: right;
    color: var(--white);
    font-weight: 600;
    font-size: 23px;
    line-height: 31px;
    letter-spacing: 0.6px;
  }
</style>
</head>
<body>
  <div class="canvas">
    <section class="card" aria-label="Business card">
      <div class="logo-frame"></div>
      <div class="logo-panel">
        <span class="logo-dot"></span>
        <span class="logo-name">Bright Fern Realty</span>
      </div>
      <div class="name-band">
        <h1 class="person-name">Maren Holt</h1>
      </div>
      <address class="contact" style="font-style: normal;">
        <div class="contact-phone">0487 316 252 (SMS)</div>
        <div class="contact-email">hello@brightfernrealty.com.au</div>
      </address>
    </section>
  </div>
</body>
</html>
```